New boutique IT consultancy needs business card

I need a business card and logo for my IT consultancy business, called 'Quenbrylle' . I want it to make me look bigger than I am. I want it to look classy, and modern. Simple design, that will be easy for me to translate into my webpage etc. The business card should be bold, and different.

The logo should emphasise the 'y' as used in quenbrylle

Target Market(s)

IT divisions in other companies

Industry/Entity Type

Business

Contact Information for Business Card

Marcel Thornby
Director
+61 437 819 063
mthornby@quenbrylle-mail.com

```html
<!DOCTYPE html>
<html lang="en">
<head>
<meta charset="utf-8">
<title>Quenbrylle — Business Card</title>
<link rel="stylesheet" href="https://fonts.googleapis.com/css2?family=Montserrat:wght@400;500;600&display=swap">
<style>
  :root {
    --page: #ecebee;
    --card: #ffffff;
    --ink: #2a2a2c;
    --slate: #5d6164;
    --slate-light: #74787b;
    --orange: #ec5a24;
    --orange-light: #f47a4c;
    --text-grey: #3c3c3e;
  }
  * { margin: 0; padding: 0; box-sizing: border-box; }
  html, body {
    width: 1200px; height: 966px; overflow: hidden;
    background: var(--page);
    font-family: "Montserrat", sans-serif;
  }
  .canvas { position: relative; width: 1200px; height: 966px; }
  .card {
    position: absolute; width: 572px; height: 370px;
    background: var(--card); overflow: hidden;
    box-shadow: 0 2px 6px rgba(0,0,0,0.12);
  }
  .card--front { left: 156px; top: 134px; }
  .card--back { left: 476px; top: 458px; }
  .card svg.bands { position: absolute; inset: 0; }
  .wordmark {
    position: absolute; left: 0; right: 0; text-align: center;
    font-weight: 600; color: var(--ink); letter-spacing: 6px;
    text-transform: uppercase;
  }
  .card--front .wordmark { top: 42px; font-size: 44px; }
  .card--back .wordmark { top: 142px; font-size: 52px; }
  .identity {
    position: absolute; right: calc(572px - 274px); top: 206px; text-align: right;
  }
  .identity__name {
    font-size: 29px; font-weight: 500; color: var(--orange);
    letter-spacing: 0.5px; text-transform: uppercase; line-height: 1.1;
  }
  .identity__role {
    font-size: 17px; font-weight: 400; color: var(--text-grey);
    letter-spacing: 0.5px; text-transform: uppercase; margin-top: 4px;
  }
  .contacts {
    position: absolute; left: 312px; top: 208px; list-style: none;
    font-size: 13.5px; color: var(--text-grey);
  }
  .contacts li { display: flex; align-items: center; gap: 9px; height: 28px; }
  .contacts svg { width: 18px; height: 18px; flex: none; }
</style>
</head>
<body>
<div class="canvas">

  <section class="card card--front">
    <svg class="bands" width="572" height="370" viewBox="0 0 572 370">
      <defs>
        <linearGradient id="frontOrange" x1="0" x2="1">
          <stop offset="0" stop-color="#f47a4c"/><stop offset="1" stop-color="#ec5a24"/>
        </linearGradient>
      </defs>
      <rect x="0" y="143" width="290" height="3" fill="var(--slate)"/>
      <rect x="290" y="143" width="282" height="3" fill="var(--orange)"/>
      <polygon points="0,334 318,334 300,370 0,370" fill="url(#frontOrange)"/>
      <polygon points="318,334 572,334 572,370 300,370" fill="var(--slate)"/>
    </svg>
    <div class="wordmark">Quenbrylle</div>
    <div class="identity">
      <div class="identity__name">Marcel Thornby</div>
      <div class="identity__role">Director</div>
    </div>
    <ul class="contacts">
      <li>
        <svg viewBox="0 0 20 20" aria-hidden="true"><circle cx="10" cy="10" r="8.5" fill="none" stroke="#3c3c3e" stroke-width="1.3"/><path d="M7 5.8c.6-.4 1.2.1 1.5.8l.4 1c.2.5 0 .9-.4 1.2.4 1 1.2 1.8 2.2 2.3.3-.4.8-.6 1.2-.4l1 .5c.6.3 1 .9.6 1.5-.5.7-1.4 1-2.3.7-2.4-.9-4.1-2.7-4.8-5-.2-.9.1-2 .6-2.6z" fill="none" stroke="#3c3c3e" stroke-width="1.1"/></svg>
        <span>+61 437 819 063</span>
      </li>
      <li>
        <svg viewBox="0 0 20 20" aria-hidden="true"><rect x="2" y="4.5" width="16" height="11" fill="none" stroke="#3c3c3e" stroke-width="1.3"/><path d="M2 4.5l8 6.5 8-6.5M2 15.5l6-5.5M18 15.5l-6-5.5" fill="none" stroke="#3c3c3e" stroke-width="1.1"/></svg>
        <span>mthornby@quenbrylle-mail.com</span>
      </li>
    </ul>
  </section>

  <section class="card card--back">
    <svg class="bands" width="572" height="370" viewBox="0 0 572 370">
      <defs>
        <linearGradient id="backSlate" x1="0" x2="1">
          <stop offset="0" stop-color="#6b6f72"/><stop offset="1" stop-color="#55595c"/>
        </linearGradient>
        <linearGradient id="backOrangeTop" x1="0" x2="1">
          <stop offset="0" stop-color="#f06a38"/><stop offset="1" stop-color="#e45726"/>
        </linearGradient>
        <linearGradient id="backOrangeBottom" x1="0" x2="1">
          <stop offset="0" stop-color="#f47a4c"/><stop offset="1" stop-color="#ee6232"/>
        </linearGradient>
      </defs>
      <polygon points="0,0 318,0 300,34 0,34" fill="url(#backSlate)"/>
      <polygon points="318,0 572,0 572,34 300,34" fill="url(#backOrangeTop)"/>
      <rect x="0" y="34" width="572" height="3" fill="var(--orange)"/>
      <rect x="0" y="330" width="572" height="3" fill="var(--orange)"/>
      <polygon points="0,333 298,333 278,370 0,370" fill="url(#backOrangeBottom)"/>
      <polygon points="298,333 572,333 572,370 278,370" fill="url(#backSlate)"/>
    </svg>
    <div class="wordmark">Quenbrylle</div>
  </section>

</div>
</body>
</html>
```